Veltrane CRM Sales Brochure

We need a sales brochure to be designed to help us promote our Orbalux C.R.M. (Customer Relationship Management) products and services. Designs aren't limited to just one side. We'd like to see professional, yet creative and fun design concepts incorporating the logo branding. Our target market will be both "White Collar" industry (Accountants / Solicitors / Business Insurance Agencies) as well as "Blue Collar" Industry (Manufacturing / Construction / Electricians). The final design should communicate our business as an experienced provider of Orbalux C.R.M. solutions. Attached files include Logo and Draft Content

```html
<!DOCTYPE html>
<html lang="en">
<head>
<meta charset="utf-8">
<title>Veltrane CRM Sales Brochure</title>
<link rel="stylesheet" href="https://fonts.googleapis.com/css2?family=Open+Sans:wght@400;600&family=Saira+Condensed:wght@500;600;700&display=swap">
<style>
:root{
  --sky:#4cc6f1;
  --charcoal:#333132;
  --slate:#5f5f5f;
  --stone:#9c9c9c;
  --mist:#8a8a8a;
  --ink:#2b2b2b;
  --paper:#ffffff;
  --backdrop:#e8e6e2;
}
*{box-sizing:border-box;margin:0;padding:0}
html,body{width:1200px;height:932px;overflow:hidden;background:var(--backdrop)}
body{position:relative;font-family:"Open Sans",sans-serif;color:var(--ink)}
.page{position:absolute;top:61px;width:546px;height:774px;background:var(--paper);overflow:hidden;box-shadow:0 2px 8px rgba(0,0,0,.18)}
.page--front{left:32px}
.page--back{left:614px}
.abs{position:absolute}
.body-copy{font-size:7.8px;line-height:12px;text-align:justify}
.body-copy p+p{margin-top:12px}

/* front */
.hero-band{left:0;top:0;width:390px;height:132px}
.hero-title{left:38px;top:22px;font-family:"Saira Condensed",sans-serif;font-weight:700;color:#fff;line-height:1}
.hero-title .lead{display:block;font-size:42px;letter-spacing:.5px}
.hero-title .line{display:block;font-size:24px;margin-top:3px;letter-spacing:.2px}
.hero-title .line--accent{color:var(--sky)}
.brand{left:400px;top:34px;width:138px;text-align:center}
.brand-mark{display:block;width:40px;height:40px;margin:0 auto 10px;background:var(--sky)}
.brand-name{font-weight:400;font-size:22px;letter-spacing:3px;color:#555}
.intro-column{left:42px;top:166px;width:207px}
.photo{background:linear-gradient(135deg,#dfe6ec,#9fb0bf 60%,#c9b7a4)}
.photo--agent{left:274px;top:163px;width:172px;height:108px;border-radius:8px}
.photo--owner{left:0;top:631px;width:220px;height:143px;border-radius:0 8px 0 0;background:linear-gradient(135deg,#6b5a48,#a08c74 50%,#d8d1c6)}
.callout{left:264px;top:296px;width:282px;height:216px;background:var(--sky);border-radius:8px 0 0 8px;padding:22px 26px 0 18px;color:#fff;font-weight:600}
.callout p{font-size:7.8px;line-height:12px;text-align:justify}
.callout p+p{margin-top:12px}

/* back */
.overview{left:33px;top:47px;width:234px}
.topic{left:32px;width:234px}
.topic-banner{position:relative;width:206px;height:20px;padding-left:8px;font-family:"Saira Condensed",sans-serif;font-weight:600;font-size:13px;line-height:20px;color:#fff;clip-path:polygon(0 0,92% 0,100% 50%,92% 100%,0 100%)}
.topic-banner--marketing{background:var(--sky)}
.topic-banner--sales{background:var(--mist)}
.topic-banner--service{background:#555}
.topic .body-copy{margin-top:18px}
.platform{left:56px;top:557px;display:flex;align-items:center;gap:10px}
.platform-mark{width:24px;height:30px;background:#1f2a5c}
.platform-name{font-weight:400;font-size:19px;line-height:23px;color:#1f2a5c}
.services{left:309px;top:32px;display:grid;grid-template-columns:93px 93px;column-gap:10px;row-gap:12px}
.service{width:93px;height:87px;background:var(--sky);border-radius:9px;text-align:center;color:#fff;padding-top:8px}
.service-name{font-family:"Saira Condensed",sans-serif;font-weight:600;font-size:13px;line-height:14px;height:28px}
.service-name--small{font-size:11px;line-height:13px}
.service svg{display:block;margin:2px auto 0;width:40px;height:40px}
.partner-badge{left:358px;top:661px;width:136px;height:36px;border-radius:4px;background:#d9d9d9}
.website{left:266px;top:707px;display:flex;align-items:center;gap:16px}
.website-name{font-weight:600;font-size:21px;color:#444}
</style>
</head>
<body>

<section class="page page--front">
  <svg class="abs hero-band" viewBox="0 0 390 132" aria-hidden="true"><polygon points="0,0 388,0 364,132 0,132" fill="var(--charcoal)"/></svg>
  <h1 class="abs hero-title">
    <span class="lead">ENHANCE</span>
    <span class="line">YOUR CUSTOMER EXPERIENCES</span>
    <span class="line line--accent">TO GROW YOUR BUSINESS FASTER</span>
  </h1>
  <div class="abs brand"><span class="brand-mark"></span><span class="brand-name">VELTRANE</span></div>

  <div class="abs body-copy intro-column">
    <p>Leveraging existing customer value via a tailored Customer Relationship Management (CRM) system is far more cost effective than prospecting for new customers. In simple terms, CRM is a technological strategy focused on managing ongoing relationships with your customers to ensure they are provided with the information they seek to enable them to purchase at the time they choose.</p>
    <p>In a digitally connected world, customer purchase perceptions are forming pre, during and post their interaction with your brand. Customers are seeking to be satisfied with the quality of your products and services, but a complicated sales process or poor service engagement will worsen overall impressions typically resulting in the likelihood of no sales transactions.</p>
    <p>CRM is the art/act of developing a working relationship with your customers, where they feel a sense of individual importance. CRM solutions increase your profitability by streamlining administrative processes in your sales, marketing, and service divisions, and letting you focus on building and maintaining the customer relationships that matter. A strong CRM solution is a multifaceted platform where everything crucial to developing, improving, and retaining your customer relationships is stored.</p>
    <p>Without the support of an integrated CRM solution, you may miss growth opportunities and lose revenue because you're not optimizing your operating processes or making the most of your customer relationships or sales leads.</p>
  </div>

  <div class="abs photo photo--agent" role="img" aria-label="Photo of a support agent wearing a headset at a computer"></div>

  <svg class="abs" style="left:0;top:0" width="546" height="774" aria-hidden="true">
    <rect x="504" y="141" width="60" height="60" rx="7" fill="var(--sky)"/>
    <rect x="475" y="216" width="90" height="51" rx="7" fill="var(--stone)"/>
    <rect x="335" y="546" width="70" height="52" rx="4" fill="var(--stone)"/>
    <rect x="430" y="540" width="130" height="24" fill="var(--slate)"/>
    <rect x="260" y="625" width="300" height="150" fill="var(--sky)"/>
    <rect x="340" y="670" width="220" height="105" fill="var(--stone)"/>
    <rect x="420" y="715" width="140" height="60" fill="var(--paper)"/>
  </svg>

  <div class="abs callout">
    <p>Imagine misplacing customer contact information, only to learn that your delay resulted in losing your client to a competitor. Or, picture your top two salespeople pursuing the same prospect, resulting in an annoyed potential customer and some unfriendly, in-house competition. Without a centralized and automated CRM system, your people can lose track of customer interactions and miss business opportunities.</p>
    <p>If you want a competitive advantage in your marketplace, a tailored CRM solution is the simple answer. CRM can take the burden of managing your customers. It enables automation of your customer management processes so you can focus on what's important: leading your business to succeed.</p>
  </div>

  <div class="abs photo photo--owner" role="img" aria-label="Photo of a shop owner with arms folded in front of his store"></div>
</section>

<section class="page page--back">
  <div class="abs body-copy overview">
    <p>Veltrane are experts in tailored CRM systems to suit businesses and departments of all sizes across a wide range of Government, Commercial and Not-for-Profit industry sectors. Using the power of Orbalux Corevia 365 we are able to install and configure a flexible solution that's customizable to suit your specific requirements. You have the choice of a stand-alone application to meet the needs of a specific line of business or use multiple CRM tools that work together as a powerful integrated solution across marketing, sales and customer service.</p>
  </div>

  <div class="abs topic" style="top:208px">
    <h2 class="topic-banner topic-banner--marketing">Marketing: Enhance &amp; Nurture</h2>
    <p class="body-copy">Generate multichannel marketing campaigns, foster sales-ready leads, and align your sales and marketing teams with planning and tracking tools that integrate with your existing apps and services.</p>
  </div>
  <div class="abs topic" style="top:310px">
    <h2 class="topic-banner topic-banner--sales">Sales: Engage &amp; Connect</h2>
    <p class="body-copy">Go beyond sales automation to better understand customer needs, engage more effectively, and win more deals. Sell smarter with embedded insights, foster relationships, boost productivity and accelerate sales performance.</p>
  </div>
  <div class="abs topic" style="top:424px">
    <h2 class="topic-banner topic-banner--service">Customer Service: Foster &amp; Support</h2>
    <p class="body-copy">Deliver guided, intelligent service and support on any channel with a unique ability to work with your existing systems. Empower customers and agents with the tools they need to ensure quick and accurate resolution, every time.</p>
  </div>

  <div class="abs platform"><span class="platform-mark"></span><span class="platform-name">Orbalux<br>Corevia 365</span></div>

  <div class="abs services">
    <div class="service"><div class="service-name">BRIEFING</div>
      <svg viewBox="0 0 40 40" fill="none" stroke="#fff" stroke-width="3"><path d="M8 10h24M8 20h24M8 30h16"/></svg></div>
    <div class="service"><div class="service-name">SETUP</div>
      <svg viewBox="0 0 40 40" fill="none" stroke="#fff" stroke-width="3"><path d="M20 6v28M6 20h28"/></svg></div>
    <div class="service"><div class="service-name">CONFIGURATION</div>
      <svg viewBox="0 0 40 40" fill="none" stroke="#fff" stroke-width="3"><circle cx="20" cy="20" r="13"/><circle cx="20" cy="20" r="4" fill="#fff"/></svg></div>
    <div class="service"><div class="service-name">LIVE LAUNCH</div>
      <svg viewBox="0 0 40 40" fill="#fff"><path d="M12 7l20 13-20 13z"/></svg></div>
    <div class="service"><div class="service-name">INSTALLATION</div>
      <svg viewBox="0 0 40 40"><rect x="3" y="15" width="34" height="10" rx="5" fill="none" stroke="#fff" stroke-width="2.5"/><rect x="6" y="18" width="20" height="4" rx="2" fill="#fff"/></svg></div>
    <div class="service"><div class="service-name">TRAINING</div>
      <svg viewBox="0 0 40 40" fill="none" stroke="#fff" stroke-width="3"><rect x="5" y="7" width="30" height="20" rx="2"/><path d="M14 34h12M20 27v7"/></svg></div>
    <div class="service"><div class="service-name">SUPPORT</div>
      <svg viewBox="0 0 40 40" fill="none" stroke="#fff" stroke-width="3"><circle cx="20" cy="20" r="14"/><path d="M20 12v10M20 27v2"/></svg></div>
    <div class="service"><div class="service-name service-name--small">CUSTOM CODING<br>&amp; DEVELOPMENT</div>
      <svg viewBox="0 0 40 40" fill="none" stroke="#fff" stroke-width="3"><path d="M14 12l-8 8 8 8M26 12l8 8-8 8"/></svg></div>
    <div class="service"><div class="service-name">INTEGRATION</div>
      <svg viewBox="0 0 40 40" fill="none" stroke="#fff" stroke-width="3"><circle cx="14" cy="20" r="8"/><circle cx="26" cy="20" r="8"/></svg></div>
    <div class="service"><div class="service-name">MIGRATION</div>
      <svg viewBox="0 0 40 40" fill="none" stroke="#fff" stroke-width="3"><path d="M6 14h26l-6-6M34 26H8l6 6"/></svg></div>
    <div class="service"><div class="service-name">REPORTING</div>
      <svg viewBox="0 0 40 40" fill="#fff"><rect x="7" y="22" width="6" height="12"/><rect x="17" y="14" width="6" height="20"/><rect x="27" y="6" width="6" height="28"/></svg></div>
    <div class="service"><div class="service-name">BESPOKE<br>MODULES</div>
      <svg viewBox="0 0 40 40" fill="#fff"><rect x="6" y="6" width="12" height="12"/><rect x="22" y="6" width="12" height="12"/><rect x="6" y="22" width="12" height="12"/><rect x="22" y="22" width="12" height="12" fill="none" stroke="#fff" stroke-width="2.5"/></svg></div>
  </div>

  <svg class="abs" style="left:0;top:0" width="546" height="774" aria-hidden="true">
    <rect x="0" y="690" width="60" height="14" fill="var(--slate)"/>
    <rect x="0" y="704" width="130" height="70" fill="var(--sky)"/>
    <rect x="0" y="735" width="70" height="39" fill="var(--stone)"/>
  </svg>

  <div class="abs partner-badge"></div>

  <div class="abs website">
    <svg width="36" height="36" viewBox="0 0 36 36" fill="none" stroke="var(--sky)" stroke-width="3"><circle cx="18" cy="18" r="15"/><path d="M3 18h30M18 3v30"/></svg>
    <span class="website-name">www.veltrane.com</span>
  </div>
</section>

</body>
</html>
```